STOREFRONT LIT SIGN for The Cantera Loft

A sign advertising our music academy. This sign will be hung 10 feet above the entrance of our building and will be seen by all pedestrian and vehicle traffic on Main Street Delano.

Target Market(s)

Street passerby

Industry/Entity Type

Music Training

Font styles to use
Other font styles liked:
• Creative

Colors

Designer to choose colors to be used in the design.

Requirements
Must have
• A White Background
• Dimensions: 8 ft long x 3 ft tall
• The Cantera Loft of Delano
• Lecciones de Piano, Violin, Guitarra, Voz, Trompeta y Mas
• MUSIC ACADEMY *(This should be most prominent)
• Guitar, Voice, Trumpet and More
• (661) 478-5926
• thecanteraloft.example
Nice to have
• Graphics of a piano, or guitar, or violin or trumpet or a combination of two or more

```html
<!DOCTYPE html>
<html lang="en">
<head>
<meta charset="utf-8">
<title>The Cantera Loft of Delano – Music Academy Sign</title>
<link rel="stylesheet" href="https://fonts.googleapis.com/css2?family=Arvo:wght@700&family=Bebas+Neue&family=PT+Sans:wght@700&display=swap">
<style>
  :root {
    --backdrop: #939496;
    --sign-white: #ffffff;
    --ink: #111111;
    --art-light: #d9d9d9;
    --art-dark: #2a2a2a;
  }
  * { margin: 0; padding: 0; box-sizing: border-box; }
  html, body {
    width: 1200px; height: 1200px; overflow: hidden;
    background: var(--backdrop);
  }
  .canvas {
    position: relative; width: 1200px; height: 1200px;
    background: var(--backdrop);
  }
  .sign {
    position: absolute; left: 76px; top: 392px;
    width: 1052px; height: 395px;
    background: var(--sign-white);
    color: var(--ink);
  }
  .sign-overlay {
    position: absolute; left: 0; top: 0;
    width: 1052px; height: 395px;
  }
  .studio-name {
    font-family: "Arvo", Georgia, serif;
    font-weight: 700;
    font-size: 30px;
    letter-spacing: 1px;
    fill: var(--ink);
  }
  .academy-title {
    position: absolute; left: 48px; top: 124px;
    font-family: "Bebas Neue", "Arial Narrow", sans-serif;
    font-size: 122px; line-height: 1;
    letter-spacing: 1px;
    white-space: nowrap;
  }
  .info-line {
    position: absolute; left: 65px; width: 600px;
    text-align: center;
    font-family: "PT Sans", Arial, sans-serif;
    font-weight: 700;
    line-height: 1;
    white-space: nowrap;
  }
  .lessons-es { font-size: 24px; }
  .lessons-es.first { top: 242px; }
  .lessons-es.second { top: 278px; }
  .lessons-en { top: 320px; font-size: 23px; }
  .contact { top: 353px; font-size: 23px; word-spacing: 2px; }
  .contact .gap { display: inline-block; width: 26px; }
  .instrument-art {
    position: absolute; left: 677px; top: 10px;
    width: 362px; height: 374px;
    background: radial-gradient(ellipse at 50% 50%, var(--art-dark) 0%, #6b6b6b 45%, var(--art-light) 80%, var(--sign-white) 100%);
    border-radius: 8px;
  }
</style>
</head>
<body>
<div class="canvas">
  <section class="sign">
    <svg class="sign-overlay" viewBox="0 0 1052 395" aria-hidden="false">
      <defs>
        <path id="name-arc" d="M 85 114 Q 360 14 635 114"/>
      </defs>
      <text class="studio-name">
        <textPath href="#name-arc" startOffset="50%" text-anchor="middle">CANTERA LOFT OF DELANO</textPath>
      </text>
      <g class="music-notes" fill="#111" stroke="#111">
        <ellipse cx="332" cy="122" rx="6" ry="4.5" transform="rotate(-20 332 122)" stroke="none"/>
        <line x1="337" y1="121" x2="341" y2="92" stroke-width="2.5"/>
        <line x1="341" y1="92" x2="352" y2="88" stroke-width="4"/>
        <ellipse cx="348" cy="118" rx="6" ry="4.5" transform="rotate(-20 348 118)" stroke="none"/>
        <line x1="353" y1="117" x2="356" y2="84" stroke-width="2.5"/>
        <line x1="356" y1="84" x2="372" y2="80" stroke-width="4"/>
        <ellipse cx="368" cy="114" rx="6" ry="4.5" transform="rotate(-20 368 114)" stroke="none"/>
        <line x1="373" y1="113" x2="372" y2="80" stroke-width="2.5"/>
        <ellipse cx="383" cy="128" rx="6" ry="4.5" transform="rotate(-20 383 128)" stroke="none"/>
        <line x1="388" y1="127" x2="387" y2="96" stroke-width="2.5"/>
        <path d="M 387 96 q 10 6 6 18" fill="none" stroke-width="2.5"/>
      </g>
    </svg>

    <h1 class="academy-title">MUSIC ACADEMY</h1>

    <p class="info-line lessons-es first">LECCIONES DE PIANO, VIOLIN, GUITARRA,</p>
    <p class="info-line lessons-es second">VOZ, TROMPETA y MAS</p>
    <p class="info-line lessons-en">GUITAR VOICE TRUMPET AND MORE</p>
    <p class="info-line contact">thecanteraloft.example<span class="gap"></span>(661) 478-5926</p>

    <div class="instrument-art" role="img" aria-label="Black line illustration of a trumpet, violin, guitar, curved piano keyboard and vintage microphone"></div>
  </section>
</div>
</body>
</html>
```